Corvell Bookkeeping Services business cards

looking for a double sided business card design. My logo is attached. I am looking for a design similar to the attached. Keen to see what my logo in white on the blue background would look like.

```html
<!DOCTYPE html>
<html lang="en">
<head>
<meta charset="utf-8">
<title>Corvell Bookkeeping Services – Business Cards</title>
<link href="https://fonts.googleapis.com/css2?family=Montserrat:wght@400;500;700;800&display=swap" rel="stylesheet">
<style>
  :root {
    --navy: #1f3a6e;
    --green: #9dbb3a;
    --white: #ffffff;
    --ink: #1d1d1f;
    --stage: #d9dadc;
  }
  * { box-sizing: border-box; margin: 0; padding: 0; }
  html, body { width: 1200px; height: 887px; overflow: hidden; }
  body {
    background: var(--stage);
    font-family: "Montserrat", sans-serif;
    position: relative;
  }
  .card {
    position: absolute;
    width: 560px;
    height: 320px;
    border-radius: 26px;
    overflow: hidden;
    box-shadow: 0 10px 28px rgba(0,0,0,0.18);
  }
  /* Front side */
  .card--front {
    left: 90px; top: 90px;
    background: var(--navy);
    display: flex; align-items: center; justify-content: center;
  }
  .brand {
    display: flex; align-items: center; gap: 18px;
    color: var(--white);
    font-weight: 800;
  }
  .brand__mark {
    width: 54px; height: 54px;
    background: var(--white);
  }
  .brand__name { font-size: 58px; line-height: 0.95; letter-spacing: -1px; }
  .brand__tag  { font-size: 17px; letter-spacing: 2.4px; margin-top: 6px; }

  /* Back side */
  .card--back {
    left: 550px; top: 477px;
    background: var(--white);
  }
  .back__brand {
    position: absolute; left: 34px; top: 36px;
    color: var(--navy); font-weight: 800;
  }
  .back__brand .brand__name { font-size: 44px; }
  .back__brand .brand__tag { font-size: 13px; letter-spacing: 1.8px; margin-top: 4px; }

  .person { position: absolute; left: 34px; top: 138px; }
  .person__name {
    font-weight: 800; font-size: 25px; letter-spacing: 0.5px; color: var(--navy);
  }
  .person__name span { color: var(--green); }
  .person__role { font-size: 14px; font-weight: 500; color: var(--ink); margin-top: 2px; }

  .contacts { position: absolute; left: 34px; top: 206px; list-style: none; }
  .contacts li {
    display: flex; align-items: center; gap: 9px;
    font-size: 14px; color: var(--ink); height: 21px;
  }
  .contacts svg { width: 14px; height: 14px; fill: var(--green); }

  .side-mark {
    position: absolute; right: 60px; top: 48px;
    width: 96px; height: 96px; background: var(--green);
  }
  .address {
    position: absolute; right: 36px; top: 168px;
    text-align: right; font-size: 14px; font-weight: 500; color: var(--ink); line-height: 1.35;
  }
  .bands { position: absolute; left: 0; bottom: 0; width: 560px; height: 90px; }
</style>
</head>
<body>

  <section class="card card--front" aria-label="Card front">
    <div class="brand">
      <div class="brand__mark"></div>
      <div>
        <div class="brand__name">Corvell</div>
        <div class="brand__tag">BOOKKEEPING SERVICES</div>
      </div>
    </div>
  </section>

  <section class="card card--back" aria-label="Card back">
    <div class="back__brand">
      <div class="brand__name">Corvell</div>
      <div class="brand__tag">BOOKKEEPING SERVICES</div>
    </div>

    <div class="person">
      <div class="person__name">DARA <span>WHITLOCK</span></div>
      <div class="person__role">Managing Director</div>
    </div>

    <ul class="contacts">
      <li>
        <svg viewBox="0 0 24 24"><path d="M6.6 10.8a15 15 0 0 0 6.6 6.6l2.2-2.2a1 1 0 0 1 1-.25 11.4 11.4 0 0 0 3.6.6 1 1 0 0 1 1 1V20a1 1 0 0 1-1 1A17 17 0 0 1 3 4a1 1 0 0 1 1-1h3.5a1 1 0 0 1 1 1c0 1.25.2 2.45.6 3.6a1 1 0 0 1-.25 1z"/></svg>
        (310)555-0142
      </li>
      <li>
        <svg viewBox="0 0 24 24"><path d="M2 5h20v14H2zm2 2v.5l8 5 8-5V7zm0 2.8V17h16V9.8l-8 5z"/></svg>
        info@corvellbooks.com
      </li>
      <li>
        <svg viewBox="0 0 24 24"><path d="M12 2a10 10 0 1 0 0 20 10 10 0 0 0 0-20zm6.9 6h-3a15 15 0 0 0-1.3-3.9A8 8 0 0 1 18.9 8zM12 4c.9 1.2 1.6 2.5 2 4h-4c.4-1.5 1.1-2.8 2-4zM4.3 14a8 8 0 0 1 0-4h3.4a16 16 0 0 0 0 4zm.8 2h3a15 15 0 0 0 1.3 3.9A8 8 0 0 1 5.1 16zm3-8h-3a8 8 0 0 1 4.3-3.9A15 15 0 0 0 8.1 8zM12 20c-.9-1.2-1.6-2.5-2-4h4c-.4 1.5-1.1 2.8-2 4zm2.3-6H9.7a14 14 0 0 1 0-4h4.6a14 14 0 0 1 0 4zm.3 5.9a15 15 0 0 0 1.3-3.9h3a8 8 0 0 1-4.3 3.9zm1.7-5.9a16 16 0 0 0 0-4h3.4a8 8 0 0 1 0 4z"/></svg>
        www.corvellbooks.com
      </li>
    </ul>

    <div class="side-mark"></div>
    <div class="address">2740 Linden Ave, Ste<br>210, Dallas, TX 75204</div>

    <svg class="bands" viewBox="0 0 560 90" preserveAspectRatio="none" aria-hidden="true">
      <polygon points="0,72 560,30 560,90 0,90" fill="var(--green)"/>
      <polygon points="400,44 560,12 560,90 400,90" fill="var(--navy)"/>
    </svg>
  </section>

</body>
</html>
```